Cosmetic Surgery Monthly Newsletter

- A4 fold out dm flyer (2up on A3, duplex)
- Refer to website for look and feel http://drpellworth.com.au Looking for a fresh, medical look with a corporate feel newsletter.
- Layout that can have different body of text dropped into it on different topics. These topics will also have images that will go with the relevent copy to demonstrate some of the cosmetic work being done.
Headings to have nice fresh look and feel, with body text to have light translucent colour behind text to make it look nice.
Need to incorporate social media logos - like us on Chatterbook, flocker, WorkRing, VidStream.

Target Market(s)

Target market is high end market aged anywhere between 20-50+ This cosmetic surgery is situated in a prestigous location and therefore its clients are willing to pay for Dr Pellworths many years of experience. He is highly qualified and has an excellent reputation.

Industry/Entity Type

Medical

Font styles to use
Serif

Requirements
Must have
• must be in line with the website look and feel
• Logo to come
Should not have
• large solid black areas

```html
<!DOCTYPE html>
<html lang="en">
<head>
<meta charset="utf-8">
<title>Dr Pellworth – Cosmetic Plastic Surgeon Flyer</title>
<link rel="stylesheet" href="https://fonts.googleapis.com/css2?family=Open+Sans:wght@300;400;600&display=swap">
<style>
  :root {
    --coral: #e8705c;
    --coral-light: #f3a594;
    --coral-pale: #f8c6b9;
    --panel-grey: #d8d8da;
    --ink: #2b2b2b;
    --ink-soft: #444;
    --clinic-red: #9b2a22;
    --map-tone: #dcd9d0;
    --stage: #efeeec;
    --white: #ffffff;
  }
  * { box-sizing: border-box; margin: 0; padding: 0; }
  html, body { width: 1200px; height: 963px; overflow: hidden; }
  body {
    background: var(--stage);
    font-family: "Open Sans", Arial, sans-serif;
    color: var(--ink);
  }
  .spread {
    position: absolute;
    left: 70px; top: 100px;
    width: 1060px; height: 760px;
    display: flex;
    box-shadow: 0 8px 24px rgba(0,0,0,.18);
  }
  .page { position: relative; width: 530px; height: 760px; overflow: hidden; }

  /* Back page */
  .page--back { background: var(--panel-grey); }
  .back-header { position: absolute; left: 0; top: 0; width: 530px; height: 120px; }
  .brand { position: absolute; text-align: center; width: 100%; }
  .brand__name { font-weight: 400; letter-spacing: .12em; color: var(--ink); }
  .brand__tag { font-weight: 600; letter-spacing: .42em; color: var(--ink-soft); }
  .page--back .brand { top: 42px; }
  .page--back .brand__name { font-size: 26px; }
  .page--back .brand__tag { font-size: 9.5px; margin-top: 1px; }

  .intro {
    position: absolute; left: 50px; right: 40px; top: 135px;
    font-size: 15px; line-height: 21px; color: var(--ink);
  }
  .divider { position: absolute; left: 50px; right: 40px; top: 228px; border-top: 1px solid #555; }
  .map-frame {
    position: absolute; left: 40px; top: 248px; width: 460px; height: 262px;
    border: 3px solid #b9b9bb; background: #c9c9cb; padding: 10px;
  }
  .map-fill { width: 100%; height: 100%; background: linear-gradient(135deg, #d7e3ea 0%, var(--map-tone) 30%, #e4e1d7 70%, #cfe0c6 100%); }

  .contact { position: absolute; left: 55px; right: 20px; top: 528px; }
  .contact__clinic { font-size: 18px; color: var(--clinic-red); }
  .contact__address { font-size: 16px; margin-top: 2px; color: var(--ink); white-space: nowrap; }
  .contact__phones { display: flex; gap: 38px; font-size: 19px; margin-top: 22px; align-items: center; }
  .contact__phones span { display: inline-flex; align-items: center; gap: 6px; }
  .contact__links { font-size: 15px; color: var(--clinic-red); margin-top: 12px; }
  .contact__sep { color: #555; }
  .socials { display: flex; flex-wrap: wrap; gap: 8px 14px; margin-top: 14px; font-size: 13px; font-weight: 600; color: var(--ink-soft); }
  .socials span { display: inline-flex; align-items: center; gap: 5px; }
  .socials i { width: 12px; height: 12px; background: var(--coral); display: inline-block; }

  /* Front page */
  .page--front { background: linear-gradient(90deg, var(--coral-pale) 0%, var(--coral-light) 45%, var(--coral) 100%); }
  .hero { position: absolute; left: 0; top: 0; width: 530px; height: 500px; }
  .page--front .brand { top: 520px; }
  .page--front .brand__name { font-size: 34px; letter-spacing: .14em; }
  .page--front .brand__tag { font-size: 12px; letter-spacing: .44em; }
  .front-web { position: absolute; top: 612px; width: 100%; text-align: center; font-size: 19px; color: var(--white); }
  .front-call { position: absolute; top: 655px; width: 100%; text-align: center; font-size: 26px; color: var(--ink); }
  .front-call strong { font-size: 34px; font-weight: 600; color: var(--white); }
</style>
</head>
<body>
<main class="spread">
  <section class="page page--back">
    <svg class="back-header" viewBox="0 0 530 120" aria-hidden="true">
      <defs>
        <linearGradient id="hdr" x1="0" x2="1">
          <stop offset="0" stop-color="#e8705c"/><stop offset="1" stop-color="#f6b2a3"/>
        </linearGradient>
      </defs>
      <path d="M0 0 H530 V90 Q265 135 0 90 Z" fill="url(#hdr)"/>
    </svg>
    <div class="brand">
      <div class="brand__name">DR PELLWORTH</div>
      <div class="brand__tag">COSMETIC PLASTIC SURGEON</div>
    </div>
    <p class="intro">Are you interested in learning more about what we have to offer you? We are more than happy to provide additional information about our services. For more details or any other questions you have, contact us</p>
    <div class="divider"></div>
    <div class="map-frame">
      <div class="map-fill" role="img" aria-label="Street map showing the clinic location"></div>
    </div>
    <div class="contact">
      <p class="contact__clinic">Harbourview Aesthetic Renewal Clinic</p>
      <p class="contact__address">14 Harrowgate Rd, Bayview Point 2031, Sydney, Australia.</p>
      <div class="contact__phones">
        <span>
          <svg width="12" height="18" viewBox="0 0 12 18" aria-hidden="true"><rect x="1" y="1" width="10" height="16" rx="2" fill="#c9302c"/><rect x="3" y="3" width="6" height="8" fill="#fff"/></svg>
          +61 (2) 5550 1840
        </span>
        <span>
          <svg width="18" height="16" viewBox="0 0 18 16" aria-hidden="true"><rect x="1" y="6" width="16" height="9" rx="1" fill="#c9302c"/><rect x="4" y="1" width="10" height="6" fill="#f3c0b8"/></svg>
          +61 (2) 5550 1847
        </span>
      </div>
      <p class="contact__links">info@drpellworth.com.au <span class="contact__sep">|</span> www.drpellworth.com.au</p>
      <div class="socials">
        <span><i></i>flocker</span>
        <span><i></i>VidStream</span>
        <span><i></i>Chatterbook</span>
        <span><i></i>WorkRing</span>
        <span><i></i>CircleUp</span>
      </div>
    </div>
  </section>

  <section class="page page--front">
    <svg class="hero" viewBox="0 0 530 500" role="img" aria-label="Photograph of three women's faces showing stages of ageing">
      <defs>
        <linearGradient id="skin" x1="0" x2="1">
          <stop offset="0" stop-color="#f3e2da"/><stop offset=".5" stop-color="#ecd3c7"/><stop offset="1" stop-color="#e6c4b2"/>
        </linearGradient>
      </defs>
      <path d="M0 0 H530 V400 Q400 500 230 460 Q90 420 0 300 Z" fill="url(#skin)"/>
    </svg>
    <div class="brand">
      <div class="brand__name">DR PELLWORTH</div>
      <div class="brand__tag">COSMETIC PLASTIC SURGEON</div>
    </div>
    <p class="front-web">www.drpellworth.com.au</p>
    <p class="front-call">Call us today : <strong>+61 2 5550 1840</strong></p>
  </section>
</main>
</body>
</html>
```